名刺の表には基本情報、裏には提供サービスの概要、をデザイン頂きたく思います。
*表:基本情報
写真、キャッチフレーズ、肩書、名前、会社情報
*裏:サービス概要
(上記全て詳細は添付ファイルを確認下さい)
依頼詳細の通りです。
最新のクラウドサービスを活用する業務のため、先進的なデザインを希望します。またメインターゲットが、若手経営者となりますので、その点でもデザイン性は重要となりますので、よろしくお願いいたします。

パッと見た時の洗煉されたデザインが気に入りました。また縦名刺デザインでうまく写真を活用いただいたので、記憶に残るデザインだと思いました。ありがとうございます。

数多くのご提案をいただき、心から御礼申し上げます。今後も何卒よろしくお願いいたします。

```html
<!DOCTYPE html>
<html lang="ja">
<head>
<meta charset="utf-8">
<title>川村誠司 名刺</title>
<link href="https://fonts.googleapis.com/css2?family=Noto+Sans+JP:wght@300;400&display=swap" rel="stylesheet">
<style>
  :root {
    --lime: #a9c21f;
    --ink: #6a6a5e;
    --ink-soft: #7c7c70;
    --olive: #8a9a3a;
    --paper: #ffffff;
    --photo-light: #eceee8;
    --photo-mid: #c9ccc4;
  }
  html, body {
    margin: 0;
    padding: 0;
    overflow: hidden;
    background: var(--paper);
  }
  .card {
    position: relative;
    width: 726px;
    height: 1200px;
    overflow: hidden;
    background: var(--paper);
    font-family: "Noto Sans JP", sans-serif;
    color: var(--ink);
  }
  .bands {
    position: absolute;
    inset: 0;
  }
  .portrait-area {
    position: absolute;
    left: 0;
    top: 600px;
    width: 420px;
    height: 600px;
    background: radial-gradient(ellipse at 45% 55%, var(--photo-mid) 0%, var(--photo-light) 60%, var(--paper) 100%);
  }
  .name {
    position: absolute;
    right: 70px;
    top: 128px;
    margin: 0;
    font-size: 62px;
    font-weight: 400;
    letter-spacing: 0.14em;
    color: var(--ink);
  }
  .contact {
    position: absolute;
    right: 66px;
    top: 228px;
    text-align: right;
  }
  .contact p {
    margin: 0;
    font-size: 28px;
    line-height: 52px;
    white-space: nowrap;
    color: var(--ink);
  }
  .company {
    position: absolute;
    right: 66px;
    top: 350px;
    text-align: right;
  }
  .company p {
    margin: 0;
    font-size: 24px;
    line-height: 48px;
    white-space: nowrap;
    color: var(--olive);
  }
  .company .address { color: var(--ink-soft); }
  .tagline {
    position: absolute;
    right: 36px;
    top: 598px;
    margin: 0;
    writing-mode: vertical-rl;
    white-space: nowrap;
    font-size: 22px;
    font-weight: 400;
    letter-spacing: 0.06em;
    color: var(--olive);
  }
  .catch {
    position: absolute;
    right: 88px;
    top: 722px;
    margin: 0;
    writing-mode: vertical-rl;
    white-space: nowrap;
    font-size: 31px;
    font-weight: 300;
    line-height: 80px;
    letter-spacing: 0.02em;
    color: var(--ink);
  }
</style>
</head>
<body>
<div class="card">
  <svg class="bands" width="726" height="1200" viewBox="0 0 726 1200" aria-hidden="true">
    <polygon points="0,0 726,0 726,22 0,262" fill="var(--lime)"/>
    <polygon points="250,1200 726,1058 726,1200" fill="var(--lime)"/>
  </svg>

  <div class="portrait-area" role="img" aria-label="タブレットを持った白いシャツの男性の写真"></div>

  <h1 class="name">川村誠司</h1>

  <div class="contact">
    <p class="phone">mobile. 090-1234-5678</p>
    <p class="email">Email. kawamura.seiji@midori-shokai.jp</p>
  </div>

  <div class="company">
    <p class="company-title">株式会社ミドリ商会 代表取締役社長</p>
    <p class="address">〒390-0811 長野県松本市中央 2-4-8</p>
  </div>

  <p class="tagline">中小企業のためのクラウドサービス導入支援の専門家</p>

  <p class="catch">経営者のお悩みを、<br>最新のクラウドサービスを<br>活用して、解決いたします！</p>
</div>
</body>
</html>
```